Modern Lawfirm Business Card Design

We're looking for a business card to incorporate the newly created logo we had made.

Ideally looking for a law firm business card demonstrating, modern, minimalist, strong/bold design.

I'm open to any design honestly, but nothing "flashy".

Target Market(s)

Immigration law, family immigration, humanitarian, general legal

Industry/Entity Type

Law Firm

Contact Information for Business Card

Please use dummy information, name, street address, city, state, phone number, email, website.

Font styles to use
Serif
Sans Serif

Requirements
Must have
• Please use dummy information, name, street address, city, state, phone number, email, website.

```html
<!DOCTYPE html>
<html lang="en">
<head>
<meta charset="utf-8">
<title>Valcourt Immigration Law – Business Card</title>
<link rel="stylesheet" href="https://fonts.googleapis.com/css2?family=Roboto:wght@400;500;700&display=swap">
<style>
  :root {
    --brand-blue: #0d5a99;
    --card-white: #f4f5f7;
    --card-shade: #dcdfe4;
    --stage: #2e2e2e;
    --ink-white: #ffffff;
  }
  * { margin: 0; padding: 0; box-sizing: border-box; }
  html, body { width: 1200px; height: 900px; overflow: hidden; }
  body {
    background: var(--stage);
    font-family: "Roboto", Arial, sans-serif;
    display: flex;
    flex-direction: column;
    align-items: center;
    justify-content: center;
    gap: 40px;
  }
  .card {
    position: relative;
    width: 700px;
    height: 390px;
    border-radius: 26px;
    overflow: hidden;
    background: linear-gradient(135deg, var(--card-white), var(--card-shade));
    box-shadow: 0 14px 30px rgba(0,0,0,.45);
  }
  .band {
    position: absolute; left: 0; top: 0;
    width: 700px; height: 390px;
  }
  .band polygon { fill: var(--brand-blue); }

  /* Front */
  .front-name {
    position: absolute; left: 44px; top: 78px;
    color: var(--ink-white);
    font-weight: 700;
    text-transform: uppercase;
  }
  .front-name .firm { display: block; font-size: 62px; letter-spacing: 3px; line-height: 1; }
  .front-name .practice { display: block; font-size: 19px; letter-spacing: 7px; margin-top: 12px; }

  /* Back */
  .back-address {
    position: absolute; left: 40px; top: 92px;
    color: var(--ink-white);
    font-style: normal;
    font-size: 19px; line-height: 1.25;
  }
  .back-name {
    position: absolute; right: 40px; top: 30px;
    color: var(--ink-white);
    font-weight: 700;
    text-transform: uppercase;
    text-align: right;
  }
  .back-name .firm { display: block; font-size: 34px; letter-spacing: 2px; line-height: 1; }
  .back-name .practice { display: block; font-size: 12px; letter-spacing: 5px; margin-top: 6px; }
  .person {
    position: absolute; left: 52px; top: 200px;
    color: var(--brand-blue);
    font-weight: 700; font-size: 19px; line-height: 1.3;
  }
  .phones {
    position: absolute; left: 52px; top: 275px;
    list-style: none;
    color: var(--brand-blue);
    font-size: 23px; font-weight: 500;
  }
  .phones li { display: flex; align-items: center; gap: 10px; margin-bottom: 6px; }
  .phones svg { width: 22px; height: 22px; }
  .web-contact {
    position: absolute; right: 40px; top: 190px;
    color: var(--brand-blue);
    font-size: 20px; line-height: 1.35;
    text-align: left;
  }
</style>
</head>
<body>
  <section class="card card-front">
    <svg class="band" viewBox="0 0 700 390" aria-hidden="true">
      <polygon points="0,0 700,0 700,120 0,330"/>
    </svg>
    <div class="front-name">
      <span class="firm">Valcourt</span>
      <span class="practice">Immigration Law</span>
    </div>
  </section>

  <section class="card card-back">
    <svg class="band" viewBox="0 0 700 390" aria-hidden="true">
      <polygon points="0,0 700,0 700,112 400,112 370,156 0,156"/>
    </svg>
    <address class="back-address">48 Sample Avenue<br>Brookdale, New York 10234</address>
    <div class="back-name">
      <span class="firm">Valcourt</span>
      <span class="practice">Immigration Law</span>
    </div>

    <div class="person">Daniel Whitmore<br>managing director</div>

    <ul class="phones">
      <li>
        <svg viewBox="0 0 22 22" aria-hidden="true"><rect width="22" height="22" rx="5" fill="var(--brand-blue)"/><path d="M5 10c0-3 12-3 12 0l-2 1.5-2-1v-1.3c-1-.4-3-.4-4 0V10.5l-2 1z" fill="#fff"/><rect x="7" y="12" width="8" height="4" rx="1" fill="#fff"/></svg>
        555 010 24 68
      </li>
      <li>
        <svg viewBox="0 0 22 22" aria-hidden="true"><rect width="22" height="22" rx="5" fill="var(--brand-blue)"/><rect x="7" y="4" width="8" height="14" rx="1.5" fill="#fff"/><rect x="8.5" y="6" width="5" height="8" fill="var(--brand-blue)"/></svg>
        555 013 57 90
      </li>
    </ul>

    <div class="web-contact">d.whitmore@valcourtimmigration.com<br>www.valcourtimmigration.com</div>
  </section>
</body>
</html>
```